Flyer Design for Private Car Service

Flyer should cater to Business Travelers and Executives who travel Business Class or First Class.
Flyer should include images attached.
Flyer should include the below text
Dallas to Austin
Chauffeured SUVs
• Travel Dallas to Austin in a new 2025 Marlow Strider for $499 one-way
• Trip includes a Uniformed Chauffeur who has a Commercial Drivers License (CDL)
• You can Schedule Chauffeur Pickup at Your Home in Dallas
• Our Chauffeur will Drop You Off at Your Final Destination in Austin
• You can Schedule Chauffeur Return Pickup in Austin and Return Back to Dallas.
• We offer Faster Times on Door-to-Door Travel than Bluecrest Airways
• We offer Comparable Prices on Door-to-Door Travel Times than Bluecrest Airways
• All of our trips are insured with $500k of commercial auto insurance
• Our Passengers can Talk on Cell Phone & Conduct Quill calls Throughout Travel
• Our Passengers have Maximum Privacy, Comfort and First-Class Amenities.
• Our Passengers Avoid Harwick Vale Field and KPR Airport hassles & delays
• Member Brenton Chamber of Commerce, Larkmoor Chamber of Commerce.
• Book your trip today at www.ridemarquel.example
Target Market(s)
Business Travelers
Look and feel
Each slider illustrates characteristics of the customer's brand and the style your logo design should communicate.

```html
<!DOCTYPE html>
<html lang="en">
<head>
<meta charset="utf-8">
<title>Dallas to Austin Chauffeured SUVs Flyer</title>
<link href="https://fonts.googleapis.com/css2?family=Archivo+Black&family=Montserrat:wght@400;600;700&family=Cabin:wght@600;700&family=Playfair+Display:ital@1&display=swap" rel="stylesheet">
<style>
:root{
  --navy-deep:#0a0f2c;
  --navy:#1b2468;
  --black:#050608;
  --gold:#b39a6e;
  --gold-light:#d9c39a;
  --cream:#efe6d6;
  --white:#ffffff;
  --photo-top:#d9d6d2;
  --photo-mid:#8a8580;
  --photo-low:#e9e0d8;
  --logo-bg:#2a2626;
  --page:#f2f2f2;
}
*{margin:0;padding:0;box-sizing:border-box}
html,body{width:1200px;height:2783px;overflow:hidden;background:var(--page)}
.flyer{position:absolute;left:50px;top:680px;width:889px;height:1150px;transform:scale(1.2373);transform-origin:0 0;overflow:hidden;background:var(--black);font-family:"Montserrat",sans-serif;color:var(--white);box-shadow:0 10px 40px rgba(0,0,0,.25)}
.header{position:absolute;left:0;top:0;width:889px;height:330px;background:linear-gradient(160deg,var(--navy-deep) 20%,var(--navy) 100%)}
.gold-band{position:absolute;right:0;top:35px;width:190px;height:75px;background:linear-gradient(90deg,#8c7447,var(--gold-light));clip-path:polygon(30% 0,100% 0,100% 100%,0 100%)}
.portrait{position:absolute;left:576px;top:42px;width:256px;height:256px;border-radius:50%;border:9px solid var(--gold);background:radial-gradient(circle at 45% 40%,#6c6a6e,#2c2a2c 70%)}
.kicker{position:absolute;left:75px;top:55px;font-size:27px;letter-spacing:7px;font-weight:400}
.from{position:absolute;left:436px;top:36px;font-family:"Playfair Display",serif;font-style:italic;font-size:42px;color:var(--cream)}
.route{position:absolute;left:105px;top:92px;font-size:34px;font-weight:700;letter-spacing:27px;color:var(--gold)}
.city{position:absolute;left:78px;top:118px;font-family:"Archivo Black",sans-serif;font-size:94px;letter-spacing:3px;line-height:1.1}
.tagline{position:absolute;left:73px;top:220px;font-size:21px;letter-spacing:3px;line-height:25px;font-weight:400}
.fleet-photo{position:absolute;left:4px;top:330px;width:885px;height:370px;background:linear-gradient(180deg,var(--photo-top) 0%,#b9b5b0 30%,var(--photo-mid) 55%,var(--photo-low) 70%,#e3d8cf 100%)}
.features{position:absolute;left:0;top:700px;width:889px;height:450px;background:linear-gradient(180deg,var(--black) 0%,#07091a 55%,#0d1237 80%,var(--black) 100%)}
.price{position:absolute;left:640px;top:625px;width:249px;height:140px;z-index:2}
.price-text{position:absolute;left:676px;top:640px;width:170px;text-align:center;line-height:1;z-index:3}
.price-text .for{font-size:21px}
.price-text .amount{font-family:"Archivo Black",sans-serif;font-size:44px;letter-spacing:3px;margin-top:3px}
.price-text .way{font-size:20px;letter-spacing:2px;margin-top:2px}
.feature{position:absolute;display:flex;align-items:center;gap:20px;font-family:"Cabin",sans-serif;font-weight:700;font-size:16px;line-height:21px}
.feature svg{width:32px;height:36px;flex:none;fill:var(--white)}
.cta{position:absolute;left:135px;top:1040px;font-weight:700;font-size:28px;letter-spacing:3px;white-space:nowrap}
.url{position:absolute;left:160px;top:1090px;font-family:"Archivo Black",sans-serif;font-size:22px;letter-spacing:1px;white-space:nowrap}
.arrow{position:absolute;left:46px;top:1092px;width:98px;height:28px}
.brand{position:absolute;left:610px;top:1012px;width:253px;height:138px;background:var(--logo-bg);display:flex;align-items:center;justify-content:center;gap:10px}
.brand-mark{width:12px;height:12px;border-radius:50%;background:var(--white);flex:none}
.brand-name{font-family:"Montserrat",sans-serif;font-weight:600;font-size:18px;letter-spacing:1.5px;color:var(--white);white-space:nowrap}
</style>
</head>
<body>
<main class="flyer">
  <section class="header">
    <div class="gold-band"></div>
    <div class="kicker">LUXURY TRAVEL</div>
    <div class="from">from</div>
    <div class="route">DALLAS TO</div>
    <h1 class="city">AUSTIN</h1>
    <p class="tagline">CHAUFFEURED SUVS FOR BUSINESS<br>CLASS AND &nbsp;FIRST- CLASS &nbsp;TRAVELERS</p>
    <div class="portrait" role="img" aria-label="Uniformed chauffeur greeting a business passenger beside a black SUV"></div>
  </section>

  <div class="fleet-photo" role="img" aria-label="Black, silver and red SUVs lined up with uniformed chauffeurs in front of a building"></div>

  <section class="features"></section>

  <svg class="price" viewBox="0 0 249 140" aria-hidden="true">
    <defs><linearGradient id="goldfade" x1="0" x2="1"><stop offset="0" stop-color="#c7ad7d"/><stop offset="1" stop-color="#6a5634"/></linearGradient></defs>
    <path d="M0 140 C25 120 30 95 40 70 C55 25 100 0 150 5 C195 10 249 20 249 20 L249 140 Z" fill="url(#goldfade)"/>
    <path d="M18 132 C40 115 45 90 55 68 C70 30 110 12 150 16 C185 20 220 40 249 48 L249 110 C220 118 190 130 150 132 C100 135 50 132 18 132 Z" fill="#0a0d22"/>
  </svg>
  <div class="price-text"><div class="for">FOR</div><div class="amount">$499</div><div class="way">ONE-WAY</div></div>

  <div class="feature" style="left:30px;top:745px"><svg viewBox="0 0 32 36"><rect x="8" y="0" width="16" height="6" rx="2"/><circle cx="16" cy="11" r="6"/><path d="M3 36V25q0-6 7-7h12q7 1 7 7v11Z"/></svg><span>Schedule Chauffeur Pickup at<br>Your Home in Dallas</span></div>
  <div class="feature" style="left:30px;top:802px"><svg viewBox="0 0 32 36"><path d="M9 2a6 6 0 0 0-6 6c0 5 6 11 6 11s6-6 6-11a6 6 0 0 0-6-6Zm0 8a2 2 0 1 1 0-4 2 2 0 0 1 0 4Z"/><path d="M23 14a5 5 0 0 0-5 5c0 4 5 9 5 9s5-5 5-9a5 5 0 0 0-5-5Zm0 7a2 2 0 1 1 0-4 2 2 0 0 1 0 4Z"/></svg><span>Drop Off at Your Final<br>Destination in Austin</span></div>
  <div class="feature" style="left:30px;top:858px"><svg viewBox="0 0 32 36"><path d="M6 12h16a7 7 0 0 1 0 14h-8v-4h8a3 3 0 0 0 0-6H6v4L0 14l6-6Z"/><rect x="6" y="22" width="8" height="8"/></svg><span>Chauffeur Return Pickup in<br>Austin to Dallas</span></div>
  <div class="feature" style="left:30px;top:922px"><svg viewBox="0 0 32 36"><rect x="12" y="2" width="18" height="18"/><circle cx="8" cy="14" r="4"/><path d="M2 36V22h12v14Z"/><rect x="20" y="24" width="8" height="10"/></svg><span>Faster Door-to-Door Travel than<br>Bluecrest Airways</span></div>
  <div class="feature" style="left:30px;top:984px"><svg viewBox="0 0 32 36"><path d="M16 2a11 11 0 0 0-11 11c0 9 11 21 11 21s11-12 11-21A11 11 0 0 0 16 2Zm0 15a4 4 0 1 1 0-8 4 4 0 0 1 0 8Z"/></svg><span>Avoid Harwick Vale Field and KPR<br>Airport Hassles &amp; Delays</span></div>

  <div class="feature" style="left:449px;top:747px"><svg viewBox="0 0 32 36"><path d="M12 2h8l-2 5h-4Z"/><path d="M14 8h4c6 3 8 8 8 13H6c0-5 2-10 8-13Z"/><path d="M0 28l8-4h10v3H9l-4 7Z"/></svg><span>Comparable Prices to<br>Bluecrest Airways</span></div>
  <div class="feature" style="left:449px;top:815px"><svg viewBox="0 0 32 36"><path d="M16 1 3 6v10c0 9 6 15 13 18 7-3 13-9 13-18V6Zm0 4 9 3v8c0 7-4 12-9 14-5-2-9-7-9-14V8Z"/><circle cx="16" cy="17" r="5"/></svg><span>$500k Commercial Auto<br>Insurance Coverage</span></div>
  <div class="feature" style="left:449px;top:890px"><svg viewBox="0 0 32 36"><circle cx="16" cy="5" r="4"/><path d="M10 16q0-6 6-6t6 6Z"/><circle cx="16" cy="24" r="7"/><circle cx="4" cy="28" r="3"/><circle cx="28" cy="28" r="3"/><path d="M0 36q0-4 4-4t4 4Zm24 0q0-4 4-4t4 4Z"/></svg><span>Talk on Cell Phone &amp; Conduct<br>Quill Calls Throughout Travel</span></div>
  <div class="feature" style="left:449px;top:962px"><svg viewBox="0 0 32 36"><path d="M3 2h16l6 6v8h-3V10h-5V5H6v26h10v3H3Z"/><circle cx="11" cy="16" r="3"/><rect x="18" y="24" width="12" height="10" rx="1"/><path d="M21 24v-3a3 3 0 0 1 6 0v3h-2v-3a1 1 0 0 0-2 0v3Z"/></svg><span>Maximum Privacy, Comfort,<br>and First-Class Amenities</span></div>

  <div class="cta">Book your trip today at</div>
  <svg class="arrow" viewBox="0 0 98 28" aria-hidden="true"><path d="M0 9h62V0l36 14-36 14v-9H0Z" fill="#ffffff"/></svg>
  <div class="url">www.ridemarquel.example</div>

  <div class="brand"><span class="brand-mark"></span><span class="brand-name">MARQUEL RIDES</span></div>
</main>
</body>
</html>
```